Fern Guildworks Business Cards

Looking or a business card design for my start-up, called "Fern Guildworks".
Our tagline is "Growing the good in people through learning, teamwork, and shared purpose."
Our mission-driven work includes professional/personal development workshops, educational design services, organizational & project management consulting, and coaching services for K-12 schools, organizations, and individuals.
You can check out the website we're building at fernguildworks.com
I select projects from designers who are highly responsive to feedback, engage in dialog about revisions, and provide all root/source documents (so please state in your initial submission that you agree to do so).
Looking forward to seeing your great designs!!
Updates
Hello everyone,
Industry/Entity Type
Building
Requirements
Must have
- Looking for a two sided design that includes our logo (I am uploading two variations that I would like incorporated in .ai format) and website on both sides.
The front side must include:
Logo, Name, Title, Phone, Email, Twitter handle
The back side must include: Logo, @ferngild (our organizational twitter handle)
Nice to have
- I like the rounded corner business cards, but that is not absolutely essential.
Should not have
- Colors beyond those presented in our logo.

```html
<!DOCTYPE html>
<html lang="en">
<head>
<meta charset="utf-8">
<title>Fern Guildworks Business Cards</title>
<link href="https://fonts.googleapis.com/css2?family=Cormorant+Garamond:wght@400;500&display=swap" rel="stylesheet">
<style>
  :root {
    --stage: #1c1c1c;
    --card-dark: #2c2827;
    --card-light: #ffffff;
    --sky: #7ccfe0;
    --stone: #b3aca4;
    --ink-soft: #9c958e;
    --rule: #d9d5d0;
    --serif: "Cormorant Garamond", Georgia, serif;
  }
  * { box-sizing: border-box; margin: 0; padding: 0; }
  html, body {
    width: 1200px; height: 1200px; overflow: hidden;
    background: var(--stage);
    font-family: var(--serif);
  }
  .canvas { position: relative; width: 1200px; height: 1200px; }

  .card {
    position: absolute; left: 220px; width: 760px; height: 434px;
    border-radius: 6px; overflow: hidden;
  }

  /* Back side */
  .card-back { top: 100px; background: var(--card-dark); text-align: center; }
  .card-back .mark {
    width: 120px; height: 120px; border-radius: 50%;
    background: var(--sky); margin: 44px auto 22px;
  }
  .card-back .brand {
    font-size: 50px; font-weight: 500; color: var(--stone);
    letter-spacing: 2px; text-transform: uppercase; line-height: 1;
  }
  .card-back .tagline {
    margin: 10px auto 0; width: 540px;
    font-size: 17px; color: var(--stone); letter-spacing: 1.5px;
    text-transform: uppercase; line-height: 1.15;
  }
  .card-back .site { margin-top: 10px; font-size: 14px; color: var(--stone); }
  .card-back .handle {
    position: absolute; left: 0; right: 0; bottom: 38px;
    font-size: 22px; color: var(--stone);
    display: flex; justify-content: center; align-items: center; gap: 8px;
  }

  /* Front side */
  .card-front { top: 610px; background: var(--card-light); }
  .card-front .edge {
    position: absolute; left: 0; top: 0; bottom: 0; width: 14px;
    background: var(--sky);
  }
  .contact { position: absolute; left: 50px; top: 34px; width: 260px; }
  .contact .person { font-size: 38px; font-weight: 400; color: var(--ink-soft); line-height: 1; }
  .contact .role { font-size: 20px; color: var(--sky); margin-top: 4px; }
  .contact .address { font-size: 19px; color: var(--ink-soft); line-height: 1.15; margin-top: 24px; }
  .contact .lines {
    margin-top: 14px; width: 258px;
    border-top: 1px solid var(--rule); border-right: 1px solid var(--rule);
  }
  .contact .line {
    display: flex; align-items: center; gap: 8px;
    font-size: 20px; color: var(--ink-soft);
    height: 46px; border-bottom: 1px solid var(--rule);
  }
  .contact .key { color: var(--sky); }

  .dot { width: 12px; height: 12px; border-radius: 50%; background: var(--sky); display: inline-block; }

  .identity { position: absolute; left: 330px; right: 20px; top: 130px; text-align: center; }
  .identity .mark {
    width: 110px; height: 110px; border-radius: 50%;
    background: var(--sky); margin: 0 auto 14px;
  }
  .identity .brand {
    font-size: 36px; font-weight: 500; color: var(--ink-soft);
    letter-spacing: 1.5px; text-transform: uppercase; line-height: 1;
  }
  .identity .pillars {
    font-size: 13px; color: var(--stone); letter-spacing: 4px;
    text-transform: uppercase; margin-top: 6px;
  }
  .identity .site { font-size: 11px; color: var(--stone); margin-top: 6px; }
</style>
</head>
<body>
<main class="canvas">

  <section class="card card-back" aria-label="Card back">
    <div class="mark"></div>
    <h1 class="brand">Fern Guildworks</h1>
    <p class="tagline">Growing the good in people through learning, teamwork, and shared purpose</p>
    <p class="site">www.fernguildworks.com</p>
    <p class="handle"><span class="dot"></span>@ferngild</p>
  </section>

  <section class="card card-front" aria-label="Card front">
    <div class="edge"></div>
    <div class="contact">
      <h2 class="person">Nora T. Hale</h2>
      <p class="role">Title / Position</p>
      <p class="address">2207 Marlow Ln<br>Dunmore, OH 45210</p>
      <div class="lines">
        <p class="line"><span class="key">P</span>+1 555-014-2290</p>
        <p class="line"><span class="key">E</span>nh@fernguildworks.com</p>
        <p class="line"><span class="dot"></span>@halenorat</p>
      </div>
    </div>
    <div class="identity">
      <div class="mark"></div>
      <p class="brand">Fern Guildworks</p>
      <p class="pillars">Leadership | Culture | Education</p>
      <p class="site">www.fernguildworks.com</p>
    </div>
  </section>

</main>
</body>
</html>
```